Flyer for Addiction program

Hi There,There are two parts to this project.1. A double-sided flyer for my next 5-day treatment program for addictions and family trauma.2. A one-page cover for the front of the course folders to match the above flyer?I have put together an information folder. Here is the filecrate link;https://www.filecrate.com/sh/jn7lkly6wcqphpt/AACmad0pag08NeuT2pM27USPa?dl=0Included in the information folder is;1. Copy2. Selection of images3. Logos and Brand identity kit4. Examples of past flyers and folder coverPlease don't hesitate to contact me if you have any questions.RegardsRebecca

Colors

Designer to choose colors to be used in the design.

Requirements
Must have
• 2 pages flyer please.
• Contemporary / fresh design

```html
<!DOCTYPE html>
<html lang="en">
<head>
<meta charset="utf-8">
<title>Unwinding the Family Pattern – Folder Covers</title>
<link rel="stylesheet" href="https://fonts.googleapis.com/css2?family=Bebas+Neue&family=Montserrat:wght@300;400;700&display=swap">
<style>
  :root {
    --stage-light: #6e6e6e;
    --stage-dark: #3d3d3d;
    --navy: #10233d;
    --paper: #ffffff;
    --mist: #eeedef;
    --stone: #a19f99;
    --ash: #d6d6d6;
    --ink: #1b1b1b;
    --label: #f2f2f2;
  }
  html, body {
    margin: 0;
    width: 1200px;
    height: 871px;
    overflow: hidden;
    background: radial-gradient(ellipse at 50% 40%, var(--stage-light), var(--stage-dark));
  }
  .board { display: block; width: 1200px; height: 871px; }
  .cover { filter: drop-shadow(0 4px 10px rgba(0,0,0,.45)); }
  .card { filter: drop-shadow(0 1px 3px rgba(0,0,0,.18)); }
  .brand-name {
    font-family: "Montserrat", sans-serif;
    font-weight: 400;
    font-size: 16px;
    letter-spacing: 3.2px;
    fill: var(--ink);
  }
  .brand-mark { fill: var(--stone); }
  .program {
    font-family: "Montserrat", sans-serif;
    font-weight: 700;
    fill: var(--ash);
  }
  .headline { font-family: "Bebas Neue", sans-serif; }
  .headline--photo { fill: url(#meadowTone); }
  .headline--navy { fill: var(--navy); }
  .headline--stone { fill: var(--stone); }
  .sample-label {
    font-family: "Montserrat", sans-serif;
    font-weight: 300;
    font-size: 31px;
    fill: var(--label);
  }
</style>
</head>
<body>
<svg class="board" viewBox="0 0 1200 871" xmlns="http://www.w3.org/2000/svg">
  <defs>
    <linearGradient id="meadowTone" x1="0" y1="0" x2="0" y2="1">
      <stop offset="0" stop-color="#d8d8d6"/>
      <stop offset="0.28" stop-color="#c9c6bf"/>
      <stop offset="0.4" stop-color="#6f7550"/>
      <stop offset="0.7" stop-color="#7e8451"/>
      <stop offset="1" stop-color="#566a36"/>
    </linearGradient>
    <linearGradient id="sunsetTone" x1="0" y1="0" x2="0" y2="1">
      <stop offset="0" stop-color="#d9c07a"/>
      <stop offset="0.5" stop-color="#efd68a"/>
      <stop offset="0.78" stop-color="#6b5a33"/>
      <stop offset="1" stop-color="#141210"/>
    </linearGradient>
  </defs>

  <!-- Cover one -->
  <g class="cover cover--one">
    <rect x="55" y="48" width="516" height="730" fill="var(--paper)"/>
    <rect x="55" y="438" width="516" height="340" fill="var(--navy)"/>
    <rect class="card" x="74" y="67" width="479" height="691" rx="12" fill="var(--paper)"/>

    <circle class="brand-mark" cx="313" cy="140" r="22"/>
    <text class="brand-name" x="313" y="210" text-anchor="middle">HALCYON COLLECTIVE</text>

    <text class="program" x="118" y="272" font-size="52" textLength="398" lengthAdjust="spacingAndGlyphs">5 DAY PROGRAM</text>

    <g role="img" aria-label="Family walking hand in hand through a grassy meadow, shown through the lettering">
      <text class="headline headline--photo" x="112" y="417" font-size="140" textLength="410" lengthAdjust="spacingAndGlyphs">UNWINDING</text>
      <text class="headline headline--photo" x="108" y="514" font-size="117" textLength="406" lengthAdjust="spacingAndGlyphs">THE FAMILY</text>
      <text class="headline headline--photo" x="108" y="652" font-size="180" textLength="410" lengthAdjust="spacingAndGlyphs">PATTERN</text>
    </g>
  </g>

  <!-- Cover two -->
  <g class="cover cover--two">
    <rect x="625" y="46" width="517" height="732" fill="var(--mist)"/>
    <rect x="625" y="438" width="517" height="340" fill="var(--navy)"/>
    <rect class="card" x="643" y="52" width="481" height="706" rx="12" fill="var(--paper)"/>

    <path d="M640 46 H1142 V160 C1120 200 1090 250 1050 275 C1000 300 950 300 900 330 C870 340 830 320 790 300 C740 285 700 260 660 250 L636 240 Z"
          fill="url(#sunsetTone)" role="img"
          aria-label="Silhouetted family at sunset: a child on a bicycle with balloons and parents lifting a child into the sky"/>

    <circle class="brand-mark" cx="884" cy="389" r="22"/>
    <text class="brand-name" x="884" y="466" text-anchor="middle">HALCYON COLLECTIVE</text>

    <text class="program" x="757" y="510" font-size="34" textLength="253" lengthAdjust="spacingAndGlyphs">5 DAY PROGRAM</text>

    <text class="headline headline--navy" x="757" y="586" font-size="80" textLength="255" lengthAdjust="spacingAndGlyphs">UNWINDING</text>
    <text class="headline headline--navy" x="757" y="644" font-size="74" textLength="253" lengthAdjust="spacingAndGlyphs">THE FAMILY</text>
    <text class="headline headline--stone" x="757" y="726" font-size="103" textLength="251" lengthAdjust="spacingAndGlyphs">PATTERN</text>
  </g>

  <text class="sample-label" x="328" y="838" text-anchor="middle">Folder Cover Sample 1</text>
  <text class="sample-label" x="892" y="838" text-anchor="middle">Folder Cover Sample 2</text>
</svg>
</body>
</html>
```